KORVEN Design

We have a 5 part framework that companies use to plot their social media strategies and digital transformation activity. We would like to display the 5 elements in a circular format (please see the attachment for our current design - we want to get a better version of that).

The five elements and their meaning can be read about here: http://plumvexstudio.example/korven/about-korven/
We would like to see designs that fit our corporate image but also maintain informality and simplicity…. Ive included another image of some of the icons we've been using and enjoying to give an understanding of the stuff we like

Target Market(s)

Corporates

Industry/Entity Type

Digital

Logo Text

Brokerage, Integration, Trust, Incentives, Leadership

Colors
0255a3

Requirements
Must have
• Must be circular in format with each element neatly labelled - PLEASE REVIEW OUR CURRENT VERSION IN THE ATTACHMENTS

```html
<!DOCTYPE html>
<html lang="en">
<head>
<meta charset="utf-8">
<title>KORVEN Framework Wheel</title>
<link rel="stylesheet" href="https://fonts.googleapis.com/css2?family=Open+Sans:wght@400;500&display=swap">
<style>
  :root {
    --page-bg: #ffffff;
    --segment-fill: #c5d2f7;
    --segment-edge: #aebde9;
    --spoke-deep: #0c2bb8;
    --spoke-bright: #0a3de6;
    --hub-ring-light: #c9cedc;
    --hub-ring-dark: #7c8499;
    --label-blue: #1b1fb0;
    --icon-navy: #26355f;
    --icon-steel: #3d7bb0;
    --hub-fill: #c3cef6;
    --hub-border: #2e3140;
    --hub-text: #ffffff;
  }
  html, body {
    margin: 0;
    padding: 0;
    width: 1200px;
    height: 1000px;
    overflow: hidden;
    background: var(--page-bg);
  }
  .framework-canvas {
    display: block;
    width: 1200px;
    height: 1000px;
  }
  .segment-label {
    font-family: "Open Sans", "Segoe UI", sans-serif;
    font-size: 40px;
    font-weight: 400;
    fill: var(--label-blue);
  }
  .hub-title {
    font-family: "Open Sans", "Segoe UI", sans-serif;
    font-size: 40px;
    font-weight: 400;
    fill: var(--hub-text);
    stroke: var(--hub-border);
    stroke-width: 1.6px;
    paint-order: stroke;
  }
  .segment { fill: var(--segment-fill); stroke: var(--segment-edge); stroke-width: 1; }
  .icon-area { fill: url(#iconTone); }
</style>
</head>
<body>
<svg class="framework-canvas" viewBox="0 0 1200 1000" xmlns="http://www.w3.org/2000/svg">
  <defs>
    <radialGradient id="spokeTone" cx="597" cy="497" r="460" gradientUnits="userSpaceOnUse">
      <stop offset="0.5" stop-color="var(--spoke-bright)"/>
      <stop offset="1" stop-color="var(--spoke-deep)"/>
    </radialGradient>
    <radialGradient id="hubRingTone" cx="597" cy="497" r="255" gradientUnits="userSpaceOnUse">
      <stop offset="0.68" stop-color="var(--hub-ring-dark)"/>
      <stop offset="1" stop-color="var(--hub-ring-light)"/>
    </radialGradient>
    <radialGradient id="hubTone" cx="0.4" cy="0.35" r="0.7">
      <stop offset="0" stop-color="#dfe6fc"/>
      <stop offset="1" stop-color="var(--hub-fill)"/>
    </radialGradient>
    <linearGradient id="iconTone" x1="0" y1="0" x2="1" y2="0">
      <stop offset="0" stop-color="var(--icon-steel)" stop-opacity="0.55"/>
      <stop offset="1" stop-color="var(--icon-navy)" stop-opacity="0.75"/>
    </linearGradient>
    <filter id="segmentShadow" x="-10%" y="-10%" width="120%" height="120%">
      <feDropShadow dx="0" dy="2" stdDeviation="3" flood-color="#1a2040" flood-opacity="0.35"/>
    </filter>
  </defs>

  <!-- Spoke band and hub ring -->
  <circle class="spoke-band" cx="597" cy="497" r="440" fill="url(#spokeTone)"/>
  <circle class="hub-ring" cx="597" cy="497" r="255" fill="url(#hubRingTone)"/>

  <!-- Framework segments -->
  <g class="segments" filter="url(#segmentShadow)">
    <path class="segment segment--brokerage" d="M389.1,88.9 A458 458 0 0 1 790.6,82 L671,338.4 A175 175 0 0 0 517.5,341.1 Z"/>
    <path class="segment segment--integration" d="M920.8,173.2 A458 458 0 0 1 1051.6,552.8 L770.7,518.3 A175 175 0 0 0 720.7,373.3 Z"/>
    <path class="segment segment--trust" d="M1012,690.6 A458 458 0 0 1 692.2,944.9 L633.4,668.2 A175 175 0 0 0 755.6,571 Z"/>
    <path class="segment segment--incentive" d="M501.8,944.9 A458 458 0 0 1 182,690.6 L438.4,571 A175 175 0 0 0 560.6,668.2 Z"/>
    <path class="segment segment--leadership" d="M144.6,568.6 A458 458 0 0 1 267.6,178.8 L471.1,375.4 A175 175 0 0 0 424.2,524.4 Z"/>
  </g>

  <!-- Segment icon areas -->
  <g class="icon-area" role="img" aria-label="Brokerage icon: row of office buildings with exchange, people, money and phone symbols">
    <rect x="505" y="135" width="180" height="105" rx="6"/>
  </g>
  <g class="icon-area" role="img" aria-label="Integration icon: two business people shaking hands with speech bubbles">
    <rect x="870" y="355" width="130" height="110" rx="6"/>
  </g>
  <g class="icon-area" role="img" aria-label="Trust building icon: person with thought bubble beside a group with a check mark">
    <rect x="718" y="720" width="140" height="80" rx="6"/>
  </g>
  <g class="icon-area" role="img" aria-label="Incentive icon: audience with chat bubbles and a rising bar chart">
    <rect x="320" y="725" width="150" height="75" rx="6"/>
  </g>
  <g class="icon-area" role="img" aria-label="Leadership icon: business person with a rising bar and line chart">
    <rect x="180" y="400" width="210" height="70" rx="6"/>
  </g>

  <!-- Segment labels -->
  <text class="segment-label" x="597" y="94" text-anchor="middle">Brokerage</text>
  <text class="segment-label" text-anchor="middle" transform="translate(862,320) rotate(-61)">Integration</text>
  <text class="segment-label" text-anchor="middle" transform="translate(857,672) rotate(26)">Trust building</text>
  <text class="segment-label" text-anchor="middle" transform="translate(333,703) rotate(-25)">Incentive</text>
  <text class="segment-label" text-anchor="middle" transform="translate(313,310) rotate(50)">Lidership</text>

  <!-- Hub -->
  <circle class="hub" cx="597" cy="497" r="172" fill="url(#hubTone)" stroke="var(--hub-border)" stroke-width="9"/>
  <circle class="hub-inner-edge" cx="597" cy="497" r="164" fill="none" stroke="#9aa3c0" stroke-width="3" opacity="0.6"/>
  <text class="hub-title" x="597" text-anchor="middle">
    <tspan x="597" y="486">Community</tspan>
    <tspan x="597" y="530">Managment</tspan>
  </text>
</svg>
</body>
</html>
```